Keynote Presentation Design Project for Crazy technology innovation company

q7ventureworks is a company that do angel investments and consult/guide technology startups. In addition i have crazy innovation projects building hardware and software for fun (like tinkerloft.example). This is not a mainstream company, but has to be serious as well as innovative. Please also look at the website design here: http://q7ventureworks.com

Please look at these projects for description for my logo design and website design for more information about the company.

website: (completed)
http://jobs.briefhive.example/job.aspx?Id=61824

logo: (completed)
http://jobs.briefhive.example/job.aspx?Id=37590

Target Market(s)

entrepreneurs & investors

Industry/Entity Type

Building

Requirements
Must have
• page designs:
All default keynote master slides should be styled.

page component designs/colour palettes:
tables
charts (up to 4 colors/rows)
process (a few boxes, arrows etc)

Delivery must be a keynote file and color codes in hex for all colors, and fonts must either be delivered or named.

```html
<!DOCTYPE html>
<html lang="en">
<head>
<meta charset="utf-8">
<title>q7ventureworks – Keynote title master</title>
<link rel="stylesheet" href="https://fonts.googleapis.com/css2?family=Yanone+Kaffeesatz:wght@400&family=Arimo:wght@400&display=swap">
<style>
  :root {
    --stage: #d9d9d9;
    --slide-bg: #f3f3f3;
    --pink: #ff3a7c;
    --blue: #1eb4ea;
    --orange: #ff8a00;
    --black: #000000;
    --white: #ffffff;
  }
  * { box-sizing: border-box; margin: 0; padding: 0; }
  html, body {
    width: 1200px; height: 1000px; overflow: hidden;
    background: radial-gradient(ellipse at center, #eeeeee 0%, var(--stage) 70%, #c4c4c4 100%);
  }
  .slide {
    position: absolute; left: 0; top: 162px;
    width: 1200px; height: 675px;
    background: var(--slide-bg);
    overflow: hidden;
  }
  .title-panel {
    position: absolute; left: 86px; top: 205px;
    width: 1028px; height: 262px;
    background: var(--pink);
    display: flex; align-items: center; justify-content: center;
  }
  .title-panel h1 {
    font-family: "Yanone Kaffeesatz", "Arial Narrow", sans-serif;
    font-weight: 400;
    font-size: 104px;
    letter-spacing: 1px;
    color: var(--white);
    text-transform: uppercase;
    line-height: 1;
  }
  .footer {
    position: absolute; left: 0; bottom: 0;
    width: 1200px; height: 45px;
    background: var(--black);
  }
  .footer-edge {
    position: absolute; left: 0; top: -8px;
    width: 1200px; height: 8px;
  }
  .swatch {
    position: absolute; bottom: 0;
    width: 28px; height: 29px;
  }
  .swatch--blue { left: 15px; background: var(--blue); }
  .swatch--pink { left: 55px; background: var(--pink); }
  .swatch--orange { left: 96px; background: var(--orange); }
  .contact {
    position: absolute; left: 0; right: 0; top: 0; height: 45px;
    display: flex; align-items: center; justify-content: center; gap: 14px;
    font-family: "Arimo", Arial, sans-serif;
    font-size: 16px; color: var(--pink);
    padding-left: 0;
  }
  .brand-mark {
    width: 26px; height: 26px; background: var(--blue);
  }
  .page-number {
    position: absolute; right: 26px; top: 0; height: 45px;
    display: flex; align-items: center;
    font-family: "Arimo", Arial, sans-serif;
    font-size: 15px; color: var(--pink);
  }
</style>
</head>
<body>
  <main class="slide">
    <section class="title-panel">
      <h1>Double-click to edit</h1>
    </section>

    <footer class="footer">
      <svg class="footer-edge" viewBox="0 0 1200 8" preserveAspectRatio="none" aria-hidden="true">
        <defs>
          <pattern id="zigzag" width="10" height="8" patternUnits="userSpaceOnUse">
            <polygon points="0,8 5,0 10,8" fill="#000000"/>
          </pattern>
        </defs>
        <rect width="1200" height="8" fill="url(#zigzag)"/>
      </svg>
      <span class="swatch swatch--blue"></span>
      <span class="swatch swatch--pink"></span>
      <span class="swatch swatch--orange"></span>
      <div class="contact">
        <span class="contact-email">info@q7ventureworks.com</span>
        <span class="brand-mark" aria-hidden="true"></span>
        <span class="contact-web">www.q7ventureworks.com</span>
      </div>
      <span class="page-number">7</span>
    </footer>
  </main>
</body>
</html>
```